Brickpress Design for a website design company

Web Design for a Web Design Company - As odd as that sounds, it is exactly right. We are a website design company with over 120 regular clients, we want to redesign our current website and take it to the next level. The problem we are finding is that we are too "inside the box". Which is why we are looking outside for a designer that will take us to the next level. We need this design to look STATE OF THE ART! Obviously there is allot we can do internally once we have a completed design to wrap up the project. So what we are looking for are some design concepts based on some ideas that we will provide. Once the concept is finalized we will need the layered design and any graphics that were used in separate files. If you have any questions please send them to us privately.

Example websites of how we want to look are:

1. http://www.brivlo.example
2. http://www.plumtavern.example
3. http://zelvaworks.example
4. http://www.kup.example
5. http://www.tarnleaf.example

Our current website we are redesigning is: www.frostlanewd.example

Navigation / Pages for new website are as follows:

Home
Services (page with broad detailing)
Portfolio
RFQ
Testimonials
About
Contact

Website Design
Website Re-design
Ecommerce
Mobile Websites
Copywriting
Hosting and Maintenance
Content Marketing
Pay Per Click Marketing
Mobile Text Marketing
Local Search Marketing

Design must be brickpress compatible, we use the meridian framework specifically.
Target Market(s)
Our target market is B2B, we want to sell web and marketing products
Requirements
Must Have:
- Design must be brickpress compatible, we use the meridian framework specifically.

As a bonus, if we like your work we may use you for our own clients...

Marcus

Industry/Entity Type

Marketing

Requirements
Must have
• For the content area - intro paragraph and blog categories below the header/banner area,

Need to include both shaded content "buttons" with graphics similar to the website attached jpg file titled - bottom content area

and hanging shaded ribbons from pixvault.example - attached jpg file titled: stock-illustration-57310268-glossy-promoting-badges

```html
<!DOCTYPE html>
<html lang="en">
<head>
<meta charset="utf-8">
<title>Frostlane Website Design</title>
<link rel="stylesheet" href="https://fonts.googleapis.com/css2?family=Open+Sans:ital,wght@0,300;0,400;0,600;1,400&display=swap">
<style>
:root{
  --ink:#2f2f2f;
  --body:#555;
  --muted:#777;
  --rule:#d9d9d9;
  --bar:#2b2b2b;
  --footer:#2a2a2a;
  --footer-text:#a9a9a9;
  --panel:#f3f3f3;
  --white:#fff;
  --brand-mark:#9a9a9a;
}
*{box-sizing:border-box;margin:0;padding:0}
html,body{width:825px;height:1200px;overflow:hidden;background:var(--white)}
body{position:relative;font-family:"Open Sans",Arial,sans-serif;color:var(--ink)}
.abs{position:absolute}

.top-bar{left:0;top:0;width:825px;height:22px;background:var(--bar)}
.social-dot{width:11px;height:11px;border-radius:50%;background:#ddd;top:5px}
.search{left:612px;top:3px;width:78px;height:16px;background:#3a3a3a;border:1px solid #555;font-size:8px;color:#bbb;padding:2px 4px;line-height:10px;white-space:nowrap;overflow:hidden}

.hero{left:0;top:22px;width:825px;height:300px;background:linear-gradient(100deg,#6b7482 0%,#8d96a3 30%,#5d6f8e 60%,#28408a 100%)}
.header-band{left:0;top:22px;width:825px;height:48px;background:rgba(255,255,255,.9)}
.logo-mark{left:112px;top:38px;width:14px;height:14px;background:var(--brand-mark)}
.logo-name{left:134px;top:31px;font-size:18px;font-weight:600;color:#555;letter-spacing:1px;line-height:1.1}
.logo-name small{display:block;font-size:10.5px;letter-spacing:0}
.nav{left:361px;top:38px;display:flex;gap:8px;font-size:12px;color:#222;white-space:nowrap}
.nav sup{font-size:7px;margin-left:1px}

.hero-title{left:106px;top:104px;font-size:37px;font-weight:600;color:var(--white);line-height:37px;letter-spacing:-1.5px}
.hero-copy{left:106px;top:188px;width:232px;font-size:8.5px;line-height:12px;color:#e8e8e8}
.hero-button{left:106px;top:259px;width:106px;height:24px;border-radius:12px;background:#222;color:var(--white);font-size:10.5px;line-height:24px;padding-left:16px;letter-spacing:.3px;white-space:nowrap}
.slide-dots{left:379px;top:303px;display:flex;gap:8px}
.slide-dots span{width:6px;height:6px;border-radius:50%;background:#ddd}
.slide-dots span.on{background:#333}

.intro-title{left:0;width:825px;top:341px;text-align:center;font-size:19px;font-weight:300}
.intro-sub{left:0;width:825px;top:367px;text-align:center;font-size:13.5px;font-style:italic;font-weight:300}

.feature-icon{width:28px;height:28px;border:1px solid #ddd;background:#fafafa;border-radius:3px}
.feature-title{font-size:12.5px;font-weight:600;white-space:nowrap}
.feature-copy{width:178px;font-size:8.2px;line-height:12px;color:var(--body)}

.section-title{font-size:14px;font-weight:300;background:var(--white);padding:0 12px;white-space:nowrap}
.section-rule{height:1px;background:var(--rule)}
.portfolio-copy{left:180px;top:597px;width:465px;text-align:center;font-size:8.3px;line-height:12px;color:var(--body)}
.portfolio-copy b{font-weight:400;color:var(--ink)}
.thumb{width:138px;height:108px;border:1px solid var(--rule);padding:4px;top:655px;background:var(--white)}
.thumb div{width:100%;height:100%}
.thumb-title{top:768px;font-size:10.8px;white-space:nowrap}
.thumb-note{top:785px;font-size:8.3px;font-style:italic;color:var(--body);white-space:nowrap}

.accordion-item{left:122px;width:278px;height:28px;background:var(--panel);border:1px solid #ddd;font-size:8.5px;color:var(--body);line-height:26px;padding-left:26px}
.accordion-item::before{content:"";position:absolute;left:13px;top:11px;border-left:3px solid #333;border-top:2.5px solid transparent;border-bottom:2.5px solid transparent}
.slider-nav{left:668px;top:836px;width:32px;height:15px;border:1px solid #bbb;display:flex}
.slider-nav span{flex:1;border-right:1px solid #bbb;font-size:7px;text-align:center;line-height:13px}
.slider-nav span:last-child{border:none}
.quote-box{left:422px;top:864px;width:278px;height:46px;border:1px solid #ddd;padding:8px 10px;font-size:8.2px;font-style:italic;line-height:12.5px;color:var(--body)}
.avatar{left:422px;top:921px;width:48px;height:48px;border-radius:50%;background:#c7ccd4;border:2px solid #ddd}
.quote-name{left:476px;top:930px;font-size:8.3px;font-weight:600}
.quote-role{left:476px;top:943px;font-size:8.3px;font-style:italic;color:var(--body)}

.footer{left:0;top:988px;width:825px;height:212px;background:var(--footer)}
.footer-text{font-size:8.3px;line-height:12px;color:var(--footer-text)}
.footer-links{left:280px;top:1012px;list-style:none;font-size:8.3px;line-height:17.2px;color:var(--footer-text);white-space:nowrap}
.footer-links li::before{content:"›";margin-right:6px;color:#666}
.post-thumb{width:42px;height:42px;border:2px solid #ddd}
.post-date{font-size:8.3px;font-style:italic;color:#ccc}
.gallery-tile{width:37px;height:37px;border:2px solid var(--white)}
.footer-rule{left:0;top:1168px;width:825px;height:1px;background:#444}
.copyright{left:122px;top:1178px;font-size:8.3px;color:#bbb;white-space:nowrap}
.copyright b,.legal-links{font-weight:600;color:#ddd}
.legal-links{left:545px;top:1178px;font-size:8.3px;display:flex;gap:10px;white-space:nowrap}
</style>
</head>
<body>

<div class="abs top-bar"></div>
<div class="abs social-dot" style="left:475px"></div>
<div class="abs social-dot" style="left:494px"></div>
<div class="abs social-dot" style="left:513px"></div>
<div class="abs social-dot" style="left:532px"></div>
<div class="abs social-dot" style="left:551px"></div>
<div class="abs social-dot" style="left:570px"></div>
<div class="abs social-dot" style="left:589px"></div>
<div class="abs search">Enter the keywo</div>

<div class="abs hero" role="img" aria-label="Blurred office interior photograph in grey and blue tones with a laptop, monitor, tablet and phone showing a responsive website"></div>
<div class="abs header-band"></div>
<div class="abs logo-mark"></div>
<div class="abs logo-name">FROSTLANE<small>Website Design</small></div>
<nav class="abs nav">
  <span>HOME<sup>v</sup></span><span>ABOUT<sup>v</sup></span><span>SERVICES<sup>v</sup></span><span>PORTFOLIO<sup>v</sup></span><span>TESTIMONIALS<sup>v</sup></span><span>FAQ<sup>v</sup></span><span>CONTACT<sup>v</sup></span>
</nav>

<h1 class="abs hero-title">Access It<br>Everywhere</h1>
<p class="abs hero-copy">Sites that adapt to every screen your clients use, from desktop monitors to tablets and phones, built responsive and fast so your brand looks sharp wherever it is opened today.</p>
<div class="abs hero-button">FOR DETAILS &#9654;</div>
<div class="abs slide-dots"><span></span><span class="on"></span><span></span></div>

<h2 class="abs intro-title">Get a professional website that gets you clients and revenue</h2>
<p class="abs intro-sub">Customised to your needs</p>

<div class="abs feature-icon" style="left:110px;top:414px">
  <svg width="28" height="28" viewBox="0 0 28 28"><circle cx="14" cy="14" r="6" fill="none" stroke="#1f8fd6" stroke-width="3.5" stroke-dasharray="3 2"/><circle cx="14" cy="14" r="2" fill="#1f8fd6"/></svg>
</div>
<div class="abs feature-title" style="left:149px;top:421px">Website Re-design</div>
<p class="abs feature-copy" style="left:111px;top:452px">We understand that consistency and perception of your product is mostly important. That's why we guarantee and ensure that our quality standard meets your need. Our quality control system guarantee you the perfection of every site we create</p>

<div class="abs feature-icon" style="left:310px;top:414px">
  <svg width="28" height="28" viewBox="0 0 28 28"><rect x="8" y="8" width="12" height="10" rx="1" fill="none" stroke="#7a3d97" stroke-width="2"/><line x1="11" y1="21" x2="17" y2="21" stroke="#7a3d97" stroke-width="2"/></svg>
</div>
<div class="abs feature-title" style="left:349px;top:421px">Mobile Websites</div>
<p class="abs feature-copy" style="left:310px;top:450px">We understand that consistency and perception of your product is mostly important. That's why we guarantee and ensure that our quality standard meets your need. Our quality control system guarantee you the perfection of every site we create</p>

<div class="abs feature-icon" style="left:512px;top:414px">
  <svg width="28" height="28" viewBox="0 0 28 28"><g fill="#f0b400"><circle cx="18" cy="8" r="3"/><circle cx="9" cy="14" r="3"/><circle cx="18" cy="20" r="3"/></g><path d="M18 8L9 14L18 20" stroke="#f0b400" stroke-width="1.5" fill="none"/></svg>
</div>
<div class="abs feature-title" style="left:550px;top:421px">Hosting and Maintenance</div>
<p class="abs feature-copy" style="left:512px;top:452px">We understand that consistency and perception of your product is mostly important. That's why we guarantee and ensure that our quality standard meets your need. Our quality control system guarantee you the perfection of every site we create</p>

<div class="abs section-rule" style="left:120px;top:576px;width:580px"></div>
<h3 class="abs section-title" style="left:333px;top:566px">Our Recent Portfolio</h3>
<p class="abs portfolio-copy">Consectetur adipiscing elit aeneane lorem lipsum, condimentum ultrices consequat eu, vehicula mauris lipsum adipiscing lipsum aenean orci lorem. Asequat lorem ipsum dolor lorem sit amet, consectetur adipiscing dolor elit. Aenean nisl orci, condimentum.Submit examples to <b>hello [at] quillmark.example</b> or tweet to <b>@thequillmark</b></p>

<div class="abs thumb" style="left:124px"><div role="img" aria-label="Country club website screenshot, dark green" style="background:linear-gradient(#2a3a14,#4f6a1c)"></div></div>
<div class="abs thumb" style="left:270px"><div role="img" aria-label="Dance studio website screenshot, orange and yellow" style="background:linear-gradient(#f3c04a,#e7852a 50%,#f6f0d8)"></div></div>
<div class="abs thumb" style="left:414px"><div role="img" aria-label="Restaurant website screenshot, cream and brown" style="background:linear-gradient(#e8d8b0,#b9863f 50%,#f1e7cf)"></div></div>
<div class="abs thumb" style="left:560px"><div role="img" aria-label="Lawn service website screenshot, green and beige" style="background:linear-gradient(#3f5a26,#7c9a52 50%,#e7dcc0)"></div></div>

<div class="abs thumb-title" style="left:124px">Ashbrook Country Club</div>
<div class="abs thumb-title" style="left:266px">StepStudio by Nia</div>
<div class="abs thumb-title" style="left:413px">Marello's Gourmet</div>
<div class="abs thumb-title" style="left:558px">Corwin's Tree and Lawn Service</div>
<div class="abs thumb-note" style="left:125px">Maecenas eu lorem leo, placera...</div>
<div class="abs thumb-note" style="left:270px">Maecenas eu lorem leo, placera...</div>
<div class="abs thumb-note" style="left:415px">Maecenas eu lorem leo, placera...</div>
<div class="abs thumb-note" style="left:560px">Maecenas eu lorem leo, placera...</div>

<div class="abs section-rule" style="left:200px;top:843px;width:200px"></div>
<h3 class="abs section-title" style="left:110px;top:834px;font-size:12.5px">Our Strength</h3>
<div class="abs accordion-item" style="top:864px">Highly Flexible</div>
<div class="abs accordion-item" style="top:893px">Fast Response</div>
<div class="abs accordion-item" style="top:922px">We customize</div>

<div class="abs section-rule" style="left:515px;top:843px;width:150px"></div>
<h3 class="abs section-title" style="left:410px;top:834px;font-size:12.5px">Our Testimonial</h3>
<div class="abs slider-nav"><span>&#9664;</span><span>&#9654;</span></div>
<div class="abs quote-box">Nullam tincidunt elit vitae dolor fringilla facilisis. Nam venenatis tempor nibh. Integer sed augue mi, vel convallis tortor.</div>
<div class="abs avatar" role="img" aria-label="Portrait photo of the client"></div>
<div class="abs quote-name">Lena Varga</div>
<div class="abs quote-role">Freelancer Web Designer</div>

<footer class="abs footer"></footer>
<p class="abs footer-text" style="left:122px;top:1010px;width:135px">Consectetur adipiscing elit aeneane lorem lipsum, condimentum ultrices consequat eu, vehicula mauris lipsum adipiscing lipsum aenean orci lorem.<br><br>Asequat lorem ipsum dolor lorem sit amet, consectetur adipiscing dolor elit. Aenean nisl orci, condimentum.</p>
<ul class="abs footer-links">
  <li>Frequently Asked Questions</li><li>Download Updates</li><li>Community Forum</li><li>Terms of Use</li><li>Privacy Policy</li>
</ul>
<div class="abs post-thumb" style="left:430px;top:1014px;background:linear-gradient(#8ea0c8,#3e4c78)" role="img" aria-label="City skyline photo"></div>
<p class="abs footer-text" style="left:483px;top:1010px;width:80px">Curabitur augue arcu consectetur adipiscing</p>
<div class="abs post-date" style="left:483px;top:1046px">July 28, 2012</div>
<div class="abs post-thumb" style="left:430px;top:1074px;background:linear-gradient(#b7c7e0,#4a5a72)" role="img" aria-label="Building photo"></div>
<p class="abs footer-text" style="left:483px;top:1071px;width:82px">Integer sed augue mi, vel convallis tortor pellentesque</p>
<div class="abs post-date" style="left:483px;top:1107px">July 28, 2012</div>

<div class="abs gallery-tile" style="left:585px;top:1010px;background:linear-gradient(135deg,#c96a1a,#3b2a12)" role="img" aria-label="Autumn leaves photo"></div>
<div class="abs gallery-tile" style="left:630px;top:1010px;background:linear-gradient(135deg,#d79a2a,#1c2a3a)" role="img" aria-label="Insect macro photo"></div>
<div class="abs gallery-tile" style="left:585px;top:1051px;background:linear-gradient(#6f95c6,#b07a3a)" role="img" aria-label="Lake sunset photo"></div>
<div class="abs gallery-tile" style="left:630px;top:1051px;background:linear-gradient(135deg,#2f6a12,#9ad03a)" role="img" aria-label="Green leaf photo"></div>
<div class="abs gallery-tile" style="left:585px;top:1092px;background:linear-gradient(#5a6a72,#1c2024)" role="img" aria-label="Forest trees photo"></div>
<div class="abs gallery-tile" style="left:630px;top:1092px;background:linear-gradient(#d8c58a,#4e5a3a)" role="img" aria-label="Landscape photo"></div>

<div class="abs footer-rule"></div>
<div class="abs copyright">Copyright ©2012-2013 <b>Halvern</b>. Designed by <b>Quillmark</b></div>
<div class="abs legal-links"><span>Sitemap</span><span>Support/Help</span><span>Terms of Usage</span></div>

</body>
</html>
```